Summit Reach Marketing
"Lifting your Brand Plans Past Every Limit"
Summit Reach Marketing - Marketing
Creative Brief
Use same font as used in my logo
Berlin
Professional
Nadia Kfoury
Marketing Consultant
Summit Reach Marketing T 961 1 847063 F 961 1 847063 M 961 3 402815 Po.Box: 738419 Beirut W http://www.summitreachmkt.me E nadiak@summitreachmkt.me E sales@summitreachmkt.me E info@summitreachmkt.me UAE | LEBANON | Summit Reach Marketing ... Lifting your Brand Plans Past Every Limit
nadia@summitreachmkt.me
on the back of the business card i want it to be in a form that ables someone to write additional notes. I maybe suggest it to be done in a form of a postcard. I suggest you check out www.summitreachmkt.me to see the spirit of the company and colors

```html
<!DOCTYPE html>
<html lang="en">
<head>
<meta charset="utf-8">
<title>Summit Reach Marketing – Stationery</title>
<link rel="stylesheet" href="https://fonts.googleapis.com/css2?family=Open+Sans:wght@400;600;700&display=swap">
<style>
  :root{
    --red:#b3121f;
    --red-dark:#8a0c16;
    --grey-curve:#e6e3e3;
    --paper:#ffffff;
    --ink:#4a4a4a;
    --ink-soft:#8d8d8d;
    --line:#d9d6d6;
    --bg:#ebe8e3;
  }
  *{box-sizing:border-box;margin:0;padding:0}
  html,body{width:1200px;height:600px;overflow:hidden}
  body{background:var(--bg);font-family:"Open Sans",Arial,sans-serif;color:var(--ink);position:relative}
  .sheet{position:absolute;background:var(--paper);box-shadow:0 2px 6px rgba(0,0,0,.18);overflow:hidden}
  .wave{position:absolute;left:0;width:100%;display:block}
  .wave.top{top:0}
  .wave.bottom{bottom:0}

  .brand{display:flex;align-items:center;gap:5px}
  .brand-dot{border-radius:50%;background:var(--red);flex:none}
  .brand-name{color:var(--red);font-weight:700;text-transform:uppercase;letter-spacing:.02em;line-height:1.1}
  .tagline{color:var(--ink-soft);font-style:normal;font-size:4px;margin-top:2px}

  .contact-list{list-style:none;color:var(--ink);line-height:1.5}
  .contact-list b{color:var(--red);font-weight:700;margin-right:3px}

  /* business card – notes back */
  .card-notes{left:20px;top:40px;width:190px;height:110px}
  .card-notes .rules{position:absolute;left:16px;right:16px;top:34px}
  .card-notes .rules span{display:block;border-bottom:1px solid var(--line);height:13px}

  /* business card – contact side */
  .card-contact{left:225px;top:40px;width:190px;height:110px;padding:24px 14px 0}
  .card-contact .person{font-size:7px;font-weight:700;color:var(--red)}
  .card-contact .role{font-size:4.5px;color:var(--ink-soft);margin-bottom:6px}
  .card-contact .contact-list{font-size:4.5px}

  /* business card – logo sides */
  .card-logo-white{left:20px;top:170px;width:190px;height:110px;display:flex;flex-direction:column;align-items:center;justify-content:center}
  .card-logo-red{left:225px;top:170px;width:190px;height:110px;background:var(--red);display:flex;flex-direction:column;align-items:center;justify-content:center}
  .card-logo-red .brand-name{color:var(--paper)}
  .card-logo-red .brand-dot{background:var(--paper)}
  .card-logo-red .tagline{color:#f0c9cc}

  /* envelope */
  .envelope{left:20px;top:296px;width:290px;height:137px;padding:12px 14px}
  .envelope .return{font-size:4px;margin-top:4px}
  .envelope .address{position:absolute;left:130px;top:64px;width:120px}
  .envelope .address span{display:block;border-bottom:1px solid var(--line);height:10px}

  /* compliment slip */
  .slip{left:140px;top:448px;width:290px;height:137px;padding:12px 14px}
  .slip .contact-list{font-size:4px;margin-top:6px}
  .slip .web{position:absolute;left:14px;bottom:6px;font-size:4.5px;color:var(--paper);z-index:2}

  /* letterhead & fax */
  .letterhead{left:460px;top:60px;width:340px;height:480px;padding:22px 24px}
  .fax{left:830px;top:60px;width:340px;height:480px;padding:22px 24px}
  .page-head{display:flex;justify-content:space-between;align-items:flex-start}
  .page-head .contact-list{font-size:4.5px;text-align:left}
  .page-web{position:absolute;left:24px;bottom:10px;font-size:5px;color:var(--paper);z-index:2}

  .fax-title{position:absolute;right:24px;top:72px;font-size:12px;font-weight:700;color:var(--red)}
  .fax-table{position:absolute;left:24px;right:24px;top:92px;border-collapse:collapse;font-size:5px;width:292px}
  .fax-table td{border:1px solid var(--line);height:15px;padding:0 4px;color:var(--ink)}
  .fax-table td.label{width:34px;color:var(--red);font-weight:600}
  .fax-checks{position:absolute;left:24px;right:24px;top:176px;display:flex;justify-content:space-between;font-size:4.5px;list-style:none}
  .fax-checks li{display:flex;align-items:center;gap:3px}
  .fax-checks li::before{content:"";width:5px;height:5px;border:1px solid var(--ink-soft)}
  .fax-rule{position:absolute;left:24px;right:24px;top:190px;border-top:1px solid var(--line)}
</style>
</head>
<body>

<!-- business card: notes back -->
<section class="sheet card-notes" aria-label="Business card back for notes">
  <svg class="wave top" viewBox="0 0 190 30" preserveAspectRatio="none" aria-hidden="true">
    <path d="M0 0H190V10C130 26 60 2 0 18Z" fill="var(--grey-curve)"/>
    <path d="M0 0H190V5C130 18 60 0 0 10Z" fill="var(--red)"/>
  </svg>
  <div class="rules"><span></span><span></span><span></span><span></span><span></span></div>
</section>

<!-- business card: contact side -->
<section class="sheet card-contact" aria-label="Business card contact side">
  <svg class="wave top" viewBox="0 0 190 22" preserveAspectRatio="none" aria-hidden="true">
    <path d="M0 0H190V12C120 22 60 4 0 10Z" fill="var(--red)"/>
  </svg>
  <p class="person">Nadia Kfoury</p>
  <p class="role">Marketing Consultant</p>
  <ul class="contact-list">
    <li><b>T</b>961 1 847063</li>
    <li><b>M</b>961 3 402815</li>
    <li><b>E</b>nadiak@summitreachmkt.me</li>
    <li><b>W</b>www.summitreachmkt.me</li>
  </ul>
</section>

<!-- business card: white logo side -->
<section class="sheet card-logo-white" aria-label="Business card logo side">
  <div class="brand"><span class="brand-dot" style="width:16px;height:16px"></span><span class="brand-name" style="font-size:9px">Summit Reach Marketing</span></div>
  <p class="tagline">"Lifting your Brand Plans Past Every Limit"</p>
</section>

<!-- business card: red logo side -->
<section class="sheet card-logo-red" aria-label="Business card red side">
  <div class="brand"><span class="brand-dot" style="width:16px;height:16px"></span><span class="brand-name" style="font-size:9px">Summit Reach Marketing</span></div>
  <p class="tagline">"Lifting your Brand Plans Past Every Limit"</p>
</section>

<!-- envelope -->
<section class="sheet envelope" aria-label="Envelope">
  <div class="brand"><span class="brand-dot" style="width:12px;height:12px"></span><span class="brand-name" style="font-size:6.5px">Summit Reach Marketing</span></div>
  <ul class="contact-list return">
    <li>Po.Box: 738419 Beirut</li>
    <li>www.summitreachmkt.me</li>
  </ul>
  <div class="address"><span></span><span></span><span></span></div>
  <svg class="wave bottom" viewBox="0 0 290 30" preserveAspectRatio="none" aria-hidden="true">
    <path d="M120 30C190 28 250 18 290 0V30Z" fill="var(--red)"/>
  </svg>
</section>

<!-- compliment slip -->
<section class="sheet slip" aria-label="Compliment slip">
  <div class="brand"><span class="brand-dot" style="width:12px;height:12px"></span><span class="brand-name" style="font-size:6.5px">Summit Reach Marketing</span></div>
  <ul class="contact-list">
    <li><b>T</b>961 1 847063</li>
    <li><b>M</b>961 3 402815</li>
    <li><b>E</b>info@summitreachmkt.me</li>
  </ul>
  <svg class="wave bottom" viewBox="0 0 290 40" preserveAspectRatio="none" aria-hidden="true">
    <path d="M0 10C90 30 200 -6 290 12V40H0Z" fill="var(--grey-curve)"/>
    <path d="M0 22C90 38 200 8 290 22V40H0Z" fill="var(--red)"/>
  </svg>
  <p class="web">http://www.summitreachmkt.me</p>
</section>

<!-- letterhead -->
<section class="sheet letterhead" aria-label="Letterhead">
  <header class="page-head">
    <div>
      <div class="brand"><span class="brand-dot" style="width:18px;height:18px"></span><span class="brand-name" style="font-size:8px">Summit Reach Marketing</span></div>
      <p class="tagline">"Lifting your Brand Plans Past Every Limit"</p>
    </div>
    <ul class="contact-list">
      <li>Po.Box: 738419 Beirut</li>
      <li><b>T</b>961 1 847063</li>
      <li><b>F</b>961 1 847063</li>
      <li><b>M</b>961 3 402815</li>
      <li><b>E</b>info@summitreachmkt.me</li>
    </ul>
  </header>
  <svg class="wave bottom" viewBox="0 0 340 70" preserveAspectRatio="none" aria-hidden="true">
    <path d="M0 20C110 50 230 -10 340 18V70H0Z" fill="var(--grey-curve)"/>
    <path d="M0 40C110 64 230 16 340 38V70H0Z" fill="var(--red)"/>
    <path d="M0 54C110 74 230 36 340 52V70H0Z" fill="var(--red-dark)"/>
  </svg>
  <p class="page-web">http://www.summitreachmkt.me</p>
</section>

<!-- fax sheet -->
<section class="sheet fax" aria-label="Fax cover sheet">
  <header class="page-head">
    <div>
      <div class="brand"><span class="brand-dot" style="width:18px;height:18px"></span><span class="brand-name" style="font-size:8px">Summit Reach Marketing</span></div>
      <p class="tagline">"Lifting your Brand Plans Past Every Limit"</p>
    </div>
    <ul class="contact-list">
      <li>Po.Box: 738419 Beirut</li>
      <li><b>T</b>961 1 847063</li>
      <li><b>F</b>961 1 847063</li>
      <li><b>M</b>961 3 402815</li>
      <li><b>E</b>sales@summitreachmkt.me</li>
    </ul>
  </header>
  <p class="fax-title">FAX</p>
  <table class="fax-table">
    <tr><td class="label">To</td><td></td><td class="label">From</td><td></td></tr>
    <tr><td class="label">Fax</td><td></td><td class="label">Pages</td><td></td></tr>
    <tr><td class="label">Phone</td><td></td><td class="label">Date</td><td></td></tr>
    <tr><td class="label">Re</td><td></td><td class="label">CC</td><td></td></tr>
  </table>
  <ul class="fax-checks">
    <li>Urgent</li><li>For Review</li><li>Please Comment</li><li>Please Reply</li>
  </ul>
  <div class="fax-rule"></div>
  <svg class="wave bottom" viewBox="0 0 340 70" preserveAspectRatio="none" aria-hidden="true">
    <path d="M0 20C110 50 230 -10 340 18V70H0Z" fill="var(--grey-curve)"/>
    <path d="M0 40C110 64 230 16 340 38V70H0Z" fill="var(--red)"/>
    <path d="M0 54C110 74 230 36 340 52V70H0Z" fill="var(--red-dark)"/>
  </svg>
  <p class="page-web">http://www.summitreachmkt.me</p>
</section>

</body>
</html>
```